PLUMBING VAN WRAP DESIGN - ROSEWOOD MECHANICAL

i have logos and basic layout for what the van wrap should look like. Everything in place can be moved around and adjusted. We want this look modern and professional. We do not want any sort of cartoon figures or any sort. The customer works on plumbing and heating and fire and ice is represented in the logo so maybe it can have that sort of feel to it. we are very open to suggestions for the final product. The logos and the slogans are import to the customer so please be as creative as you can with it.

```html
<!DOCTYPE html>
<html lang="en">
<head>
<meta charset="utf-8">
<title>Rosewood Mechanical – Van Wrap</title>
<link rel="stylesheet" href="https://fonts.googleapis.com/css2?family=Oswald:wght@500;700&display=swap">
<style>
  :root{
    --ink:#111214;
    --orange:#f4a53a;
    --orange-deep:#e98b25;
    --blue:#2f8fd8;
    --blue-sky:#3aa6e6;
    --blue-deep:#3b55b8;
    --yellow:#f3c02a;
    --steel:#b9bcc2;
    --glass:#7a7d82;
    --tyre:#1b1c1e;
    --hub:#8d9095;
    --page:#ffffff;
  }
  html,body{margin:0;padding:0;overflow:hidden;background:var(--page);}
  .canvas{width:1200px;height:1200px;position:relative;overflow:hidden;background:var(--page);}
  .van{position:absolute;left:44px;width:1112px;height:494px;}
  .van--angled{top:62px;}
  .van--classic{top:628px;}
  .label{font-family:'Oswald',sans-serif;font-weight:700;letter-spacing:.5px;}
  .services{fill:var(--ink);font-size:15px;}
  .services--open{fill:var(--blue-sky);font-size:32px;}
  .phone{fill:var(--yellow);font-size:40px;}
  .phone--open{font-size:44px;}
  .slogan{fill:var(--ink);font-size:13px;}
  .slogan--open{font-size:14px;}
  .brand{fill:var(--steel);font-size:60px;}
  .brand-sub{fill:var(--steel);font-size:34px;}
  .brand-region{fill:var(--yellow);font-size:26px;}
  .social{font-family:'Oswald',sans-serif;font-weight:500;font-size:11px;}
  .social--light{fill:var(--page);}
  .social--dark{fill:var(--ink);}
</style>
</head>
<body>
<main class="canvas">

  <!-- Angled-band wrap -->
  <svg class="van van--angled" viewBox="0 0 900 400" xmlns="http://www.w3.org/2000/svg">
    <defs>
      <linearGradient id="orangeA" x1="0" y1="0" x2="1" y2="0">
        <stop offset="0" stop-color="var(--orange-deep)"/><stop offset="1" stop-color="var(--orange)"/>
      </linearGradient>
      <linearGradient id="blueA" x1="0" y1="0" x2="1" y2="0">
        <stop offset="0" stop-color="var(--blue)"/><stop offset="1" stop-color="var(--blue-deep)"/>
      </linearGradient>
      <clipPath id="bodyA"><path d="M6,60 Q6,30 40,30 L560,25 Q615,27 650,60 L760,165 Q850,185 885,230 L895,300 L895,345 L6,345 Z"/></clipPath>
    </defs>
    <g clip-path="url(#bodyA)">
      <rect class="wrap-base" width="900" height="400" fill="url(#orangeA)"/>
      <polygon class="band-dark" points="0,62 330,100 600,110 700,130 900,200 900,400 0,400" fill="var(--ink)"/>
      <polygon class="band-ice" points="0,175 400,230 700,290 900,305 900,330 0,330" fill="url(#blueA)" role="img" aria-label="Faint snowflake texture in blues"/>
      <polygon class="band-services" points="15,45 355,97 355,113 15,63" fill="var(--blue-sky)"/>
      <polygon class="band-slogan" points="20,157 294,203 294,223 20,177" fill="var(--yellow)"/>
      <polygon class="logo-backing" points="305,140 625,140 625,275 560,302 360,302 330,270" fill="var(--ink)"/>
      <rect class="skirt" x="0" y="300" width="900" height="45" fill="var(--ink)"/>
    </g>
    <text class="label services" transform="translate(62,66) rotate(8.7)" textLength="250" lengthAdjust="spacingAndGlyphs">PLUMBING • HEATING • AIR CONDITIONING</text>
    <text class="label phone" transform="translate(61,141) rotate(6)" textLength="232" lengthAdjust="spacingAndGlyphs">907-555-0148</text>
    <text class="label slogan" transform="translate(26,173) rotate(9.5)" textLength="258" lengthAdjust="spacingAndGlyphs">BIG ENOUGH TO HELP SMALL ENOUGH TO CARE</text>
    <circle class="emblem" cx="470" cy="86" r="55" fill="var(--blue-sky)"/>
    <text class="label brand" x="314" y="203" textLength="298" lengthAdjust="spacingAndGlyphs">ROSEWOOD</text>
    <rect class="brand-rule" x="314" y="212" width="298" height="4" fill="var(--blue-sky)"/>
    <text class="label brand-sub" x="324" y="258" textLength="262" lengthAdjust="spacingAndGlyphs">MECHANICAL LLC</text>
    <text class="label brand-region" x="369" y="292" textLength="160" lengthAdjust="spacing">ALASKA</text>
    <polygon class="window" points="622,125 700,125 760,200 760,222 622,222" fill="var(--glass)"/>
    <circle cx="660" cy="254" r="6" fill="var(--page)"/>
    <text class="social social--light" x="671" y="258">@rosewoodak</text>
    <g class="wheel"><circle cx="258" cy="350" r="46" fill="var(--tyre)"/><circle cx="258" cy="350" r="22" fill="var(--hub)"/></g>
    <g class="wheel"><circle cx="774" cy="350" r="46" fill="var(--tyre)"/><circle cx="774" cy="350" r="22" fill="var(--hub)"/></g>
  </svg>

  <!-- Classic split wrap -->
  <svg class="van van--classic" viewBox="0 0 900 400" xmlns="http://www.w3.org/2000/svg">
    <defs>
      <linearGradient id="orangeB" x1="0" y1="0" x2="1" y2="0">
        <stop offset="0" stop-color="var(--orange-deep)"/><stop offset="1" stop-color="var(--orange)"/>
      </linearGradient>
      <linearGradient id="blueB" x1="0" y1="0" x2="1" y2="0">
        <stop offset="0" stop-color="var(--blue-deep)"/><stop offset="1" stop-color="var(--blue)"/>
      </linearGradient>
      <clipPath id="bodyB"><path d="M6,58 Q6,28 40,28 L560,23 Q615,25 650,58 L760,165 Q850,185 885,230 L895,300 L895,345 L6,345 Z"/></clipPath>
    </defs>
    <g clip-path="url(#bodyB)">
      <rect class="wrap-base" width="900" height="400" fill="url(#orangeB)"/>
      <polygon class="panel-dark" points="0,0 470,0 520,60 545,200 575,300 0,300" fill="var(--ink)"/>
      <polygon class="logo-backing" points="305,168 628,168 628,262 600,298 370,298 330,262" fill="var(--ink)"/>
      <rect class="band-slogan" x="36" y="233" width="272" height="26" fill="var(--yellow)"/>
      <rect class="stripe-ice" x="0" y="300" width="900" height="16" fill="url(#blueB)"/>
      <rect class="skirt" x="0" y="316" width="900" height="30" fill="var(--ink)"/>
    </g>
    <text class="label services services--open" x="172" y="97" text-anchor="middle" textLength="202" lengthAdjust="spacingAndGlyphs">PLUMBING • HEATING</text>
    <text class="label services services--open" x="172" y="126" text-anchor="middle" textLength="177" lengthAdjust="spacingAndGlyphs">AIR CONDITIONING</text>
    <text class="label phone phone--open" x="45" y="190" textLength="238" lengthAdjust="spacingAndGlyphs">907-555-0148</text>
    <text class="label slogan slogan--open" x="43" y="252" textLength="245" lengthAdjust="spacingAndGlyphs">BIG ENOUGH TO HELP SMALL ENOUGH TO CARE</text>
    <circle class="emblem" cx="470" cy="100" r="55" fill="var(--blue-sky)"/>
    <text class="label brand" x="307" y="218" textLength="300" lengthAdjust="spacingAndGlyphs">ROSEWOOD</text>
    <rect class="brand-rule" x="307" y="226" width="300" height="4" fill="var(--blue-sky)"/>
    <text class="label brand-sub" x="324" y="260" textLength="278" lengthAdjust="spacingAndGlyphs">MECHANICAL LLC</text>
    <text class="label brand-region" x="379" y="290" textLength="160" lengthAdjust="spacing">ALASKA</text>
    <polygon class="window" points="622,125 700,125 760,200 760,221 622,221" fill="var(--glass)"/>
    <circle cx="660" cy="256" r="6" fill="var(--ink)"/>
    <text class="social social--dark" x="671" y="260">@rosewoodak</text>
    <g class="wheel"><circle cx="258" cy="347" r="46" fill="var(--tyre)"/><circle cx="258" cy="347" r="22" fill="var(--hub)"/></g>
    <g class="wheel"><circle cx="774" cy="347" r="46" fill="var(--tyre)"/><circle cx="774" cy="347" r="22" fill="var(--hub)"/></g>
  </svg>

</main>
</body>
</html>
```